Facebook, Twitter and Linkedin cover image design

Looking to update the facebook, twitter and aLinkedin cover images for Tandem Accounts . website www.tandacct.example
https://www.prolinknet.example/company/tandem-accounts-llc/mycompany/?viewAsMember=true
https://www.socialpage.example/tandacct
https://chirpline.example/tandacct

```html
<!DOCTYPE html>
<html lang="en">
<head>
<meta charset="utf-8">
<title>Tandem Accounts – Social Cover Set</title>
<link href="https://fonts.googleapis.com/css2?family=League+Gothic&family=Lato:ital,wght@0,400;0,700;1,400&display=swap" rel="stylesheet">
<style>
  :root{
    --board:#434343;
    --label:#8b8b8b;
    --white:#ffffff;
  }
  *{margin:0;padding:0;box-sizing:border-box}
  html,body{width:1005px;height:1200px;overflow:hidden}
  body{background:var(--board);position:relative;font-family:"Lato",sans-serif}

  .platform-label{position:absolute;font-family:"Lato",sans-serif;font-style:italic;font-weight:400;font-size:36px;color:var(--label);line-height:1;letter-spacing:0.5px}

  .cover{position:absolute;overflow:visible}
  .cover::after{content:"";position:absolute;left:10%;right:10%;bottom:-6px;height:20px;border-radius:50%;
    box-shadow:0 14px 22px rgba(0,0,0,.55);z-index:-1}
  .cover-art{position:absolute;inset:0;width:100%;height:100%;display:block}

  .brand-row{position:absolute;display:flex;align-items:center;color:var(--white)}
  .brand{display:flex;align-items:center}
  .brand-square{background:var(--white);flex:none}
  .brand-name{font-family:"League Gothic",sans-serif;text-transform:uppercase;line-height:.9;color:var(--white)}
  .brand-divider{background:rgba(255,255,255,.75);width:1px;flex:none}
  .product-name{font-family:"League Gothic",sans-serif;color:var(--white);line-height:1}

  .sector-list{position:absolute;list-style:none;font-family:"League Gothic",sans-serif;color:var(--white);text-transform:uppercase;letter-spacing:0}
  .sector-list li{position:relative;white-space:nowrap}
  .star{position:absolute;font-family:"Lato",sans-serif;font-size:.5em}
  .inline-star{font-family:"Lato",sans-serif;font-size:.5em;margin:0 12px 0 14px;vertical-align:middle}

  .site{position:absolute;display:flex;align-items:center;color:var(--white);font-style:italic}
  .site svg{margin-right:4px}

  /* Twitter */
  .cover--twitter{left:74px;top:79px;width:857px;height:285px}
  .cover--twitter .brand-row{left:19px;top:18px;height:45px}
  .cover--twitter .brand-square{width:33px;height:33px;margin-right:5px}
  .cover--twitter .brand-name{font-size:17px}
  .cover--twitter .brand-divider{height:48px;margin:0 11px 0 12px}
  .cover--twitter .product-name{font-size:24px}
  .cover--twitter .sector-list{left:60px;top:78px;font-size:26px;line-height:32px}
  .cover--twitter .star{left:-16px;top:0}
  .cover--twitter .site{left:19px;top:250px;font-size:13px}

  /* Facebook */
  .cover--facebook{left:78px;top:462px;width:850px;height:335px}
  .cover--facebook .brand-row{left:27px;top:17px;height:52px}
  .cover--facebook .brand-square{width:36px;height:36px;margin-right:5px}
  .cover--facebook .brand-name{font-size:19px}
  .cover--facebook .brand-divider{height:52px;margin:0 11px 0 12px}
  .cover--facebook .product-name{font-size:26px}
  .cover--facebook .sector-list{left:53px;top:90px;font-size:26px;line-height:23px}
  .cover--facebook .sector-list li{margin-bottom:8px}
  .cover--facebook .star{left:-16px;top:0}
  .cover--facebook .site{left:27px;top:299px;font-size:14px}

  /* LinkedIn */
  .cover--linkedin{left:79px;top:902px;width:847px;height:211px}
  .cover--linkedin .brand-row{left:14px;top:12px;height:34px}
  .cover--linkedin .brand-square{width:25px;height:25px;margin-right:4px}
  .cover--linkedin .brand-name{font-size:13px}
  .cover--linkedin .brand-divider{height:34px;margin:0 8px 0 9px}
  .cover--linkedin .product-name{font-size:17px}
  .cover--linkedin .sector-list{left:60px;top:55px;font-size:20px;line-height:24px}
  .cover--linkedin .star{left:-12px;top:0}
  .cover--linkedin .site{left:14px;top:185px;font-size:11px}
</style>
</head>
<body>

<svg width="0" height="0" style="position:absolute" aria-hidden="true">
  <defs>
    <linearGradient id="sunset" x1="0" y1="0" x2="0" y2="1">
      <stop offset="0" stop-color="#b9b28f"/>
      <stop offset=".35" stop-color="#e7b455"/>
      <stop offset=".62" stop-color="#9c8a3c"/>
      <stop offset="1" stop-color="#2f5a22"/>
    </linearGradient>
    <radialGradient id="truck" cx=".5" cy=".5" r=".5">
      <stop offset="0" stop-color="#2f6a3a"/>
      <stop offset="1" stop-color="#2f6a3a" stop-opacity="0"/>
    </radialGradient>
    <linearGradient id="panel" x1="0" y1="0" x2="1" y2="1">
      <stop offset="0" stop-color="#5aa253"/>
      <stop offset="1" stop-color="#4a9444"/>
    </linearGradient>
    <radialGradient id="tools" cx=".5" cy=".5" r=".5">
      <stop offset="0" stop-color="#5a5a5c"/><stop offset="1" stop-color="#242426"/>
    </radialGradient>
    <radialGradient id="oil" cx=".55" cy=".45" r=".6">
      <stop offset="0" stop-color="#f0a23a"/><stop offset="1" stop-color="#6e300f"/>
    </radialGradient>
    <radialGradient id="keys" cx=".5" cy=".5" r=".5">
      <stop offset="0" stop-color="#ffffff"/><stop offset="1" stop-color="#dcdcdc"/>
    </radialGradient>
  </defs>
</svg>

<!-- Twitter -->
<h2 class="platform-label" style="left:69px;top:29px">Twitter</h2>
<section class="cover cover--twitter">
  <svg class="cover-art" viewBox="0 0 857 285" preserveAspectRatio="none">
    <g role="img" aria-label="Green semi truck on a country road at sunset">
      <rect x="380" y="0" width="477" height="285" fill="url(#sunset)"/>
      <ellipse cx="730" cy="175" rx="110" ry="100" fill="url(#truck)"/>
    </g>
    <polygon points="520,0 398,142 520,285 436,142" fill="#ffffff"/>
    <polygon points="0,0 520,0 398,142 520,285 0,285" fill="url(#panel)"/>
    <circle cx="599" cy="53" r="42" fill="url(#tools)" role="img" aria-label="Wrenches and bearings"/>
    <circle cx="517" cy="142" r="54" fill="url(#oil)" role="img" aria-label="Oil pump jack and worker at sunset"/>
    <circle cx="597" cy="229" r="43" fill="url(#keys)" role="img" aria-label="Car keys handed over"/>
  </svg>
  <div class="brand-row">
    <div class="brand"><span class="brand-square"></span><span class="brand-name">Tandem<br>Accounts</span></div>
    <span class="brand-divider"></span>
    <span class="product-name">FleetLedger</span>
  </div>
  <ul class="sector-list">
    <li><span class="star">★</span>Oil and Gas</li>
    <li><span class="star">★</span>Transporation</li>
    <li><span class="star">★</span>Repair, Parts and Tire Locations</li>
    <li><span class="star">★</span>Automative and Truck Dealership</li>
    <li><span class="star">★</span>Manufacturing and Industrial Maintenance</li>
  </ul>
  <div class="site"><svg width="12" height="12" viewBox="0 0 12 12" fill="none" stroke="#fff" stroke-width=".9"><circle cx="6" cy="6" r="5.3"/><ellipse cx="6" cy="6" rx="2.3" ry="5.3"/><path d="M.7 6h10.6M1.5 3.3h9M1.5 8.7h9"/></svg>tandacct.example</div>
</section>

<!-- Facebook -->
<h2 class="platform-label" style="left:80px;top:412px">Facebook</h2>
<section class="cover cover--facebook">
  <svg class="cover-art" viewBox="0 0 850 335" preserveAspectRatio="none">
    <g role="img" aria-label="Green semi truck on a country road at sunset">
      <rect x="300" y="0" width="550" height="335" fill="url(#sunset)"/>
      <ellipse cx="700" cy="205" rx="130" ry="120" fill="url(#truck)"/>
    </g>
    <polygon points="453,0 310,167 453,335 350,167" fill="#ffffff"/>
    <polygon points="0,0 453,0 310,167 453,335 0,335" fill="url(#panel)"/>
    <circle cx="545" cy="63" r="50" fill="url(#tools)" role="img" aria-label="Wrenches and bearings"/>
    <circle cx="450" cy="166" r="64" fill="url(#oil)" role="img" aria-label="Oil pump jack and worker at sunset"/>
    <circle cx="545" cy="270" r="50" fill="url(#keys)" role="img" aria-label="Car keys handed over"/>
  </svg>
  <div class="brand-row">
    <div class="brand"><span class="brand-square"></span><span class="brand-name">Tandem<br>Accounts</span></div>
    <span class="brand-divider"></span>
    <span class="product-name">FleetLedger</span>
  </div>
  <ul class="sector-list">
    <li><span class="star">★</span>Oil and Gas<span class="inline-star">★</span>Transporation</li>
    <li><span class="star">★</span>Repair, Parts and<br>Tire Locations</li>
    <li><span class="star">★</span>Automative and Truck<br>Dealership</li>
    <li><span class="star">★</span>Manufacturing and Industrial<br>Maintenance</li>
  </ul>
  <div class="site"><svg width="13" height="13" viewBox="0 0 12 12" fill="none" stroke="#fff" stroke-width=".9"><circle cx="6" cy="6" r="5.3"/><ellipse cx="6" cy="6" rx="2.3" ry="5.3"/><path d="M.7 6h10.6M1.5 3.3h9M1.5 8.7h9"/></svg>tandacct.example</div>
</section>

<!-- LinkedIn -->
<h2 class="platform-label" style="left:80px;top:850px">Linkedin</h2>
<section class="cover cover--linkedin">
  <svg class="cover-art" viewBox="0 0 847 211" preserveAspectRatio="none">
    <g role="img" aria-label="Green semi truck on a country road at sunset">
      <rect x="350" y="0" width="497" height="211" fill="url(#sunset)"/>
      <ellipse cx="720" cy="130" rx="110" ry="80" fill="url(#truck)"/>
    </g>
    <polygon points="452,0 361,105 452,211 385,105" fill="#ffffff"/>
    <polygon points="0,0 452,0 361,105 452,211 0,211" fill="url(#panel)"/>
    <circle cx="523" cy="41" r="31" fill="url(#tools)" role="img" aria-label="Wrenches and bearings"/>
    <circle cx="463" cy="105" r="40" fill="url(#oil)" role="img" aria-label="Oil pump jack and worker at sunset"/>
    <circle cx="522" cy="170" r="31" fill="url(#keys)" role="img" aria-label="Car keys handed over"/>
  </svg>
  <div class="brand-row">
    <div class="brand"><span class="brand-square"></span><span class="brand-name">Tandem<br>Accounts</span></div>
    <span class="brand-divider"></span>
    <span class="product-name">FleetLedger</span>
  </div>
  <ul class="sector-list">
    <li><span class="star">★</span>Oil and Gas</li>
    <li><span class="star">★</span>Transporation</li>
    <li><span class="star">★</span>Repair, Parts and Tire Locations</li>
    <li><span class="star">★</span>Automative and Truck Dealership</li>
    <li><span class="star">★</span>Manufacturing and Industrial Maintenance</li>
  </ul>
  <div class="site"><svg width="10" height="10" viewBox="0 0 12 12" fill="none" stroke="#fff" stroke-width="1"><circle cx="6" cy="6" r="5.3"/><ellipse cx="6" cy="6" rx="2.3" ry="5.3"/><path d="M.7 6h10.6M1.5 3.3h9M1.5 8.7h9"/></svg>tandacct.example</div>
</section>

</body>
</html>
```